International Wholesale Food Company Needs Packaging Design for new products

We have a logo for our new business. It is attached. Now we need a packaging design for some new products that we will be selling. These items will be packaged in clear plastic bags. We are an international wholesale foods company selling foods imported from West Africa. We are just in the process of launching. We're looking for a design that is fresh and modern.

These items below are what we need packaging design for:

Cassava Leaves-500 g- Clear Plastic Bag
Sweet potato leaves-500 g-Clear Plastic Bag

```html
<!DOCTYPE html>
<html lang="en">
<head>
<meta charset="utf-8">
<title>Sweet Potato Leaves – Package Label</title>
<link rel="stylesheet" href="https://fonts.googleapis.com/css2?family=Cinzel:wght@400;600&family=Open+Sans:wght@400;600&display=swap">
<style>
  :root {
    --bg: #f4f4f4;
    --label-white: #ffffff;
    --leaf-dark: #14622f;
    --leaf-mid: #1f7a3c;
    --leaf-light: #3a9a4e;
    --brand-red: #c41e2e;
    --title-green: #17633a;
    --body-grey: #555555;
    --seal-green: #7dbb3f;
  }
  * { box-sizing: border-box; margin: 0; padding: 0; }
  html, body {
    width: 1200px;
    height: 1200px;
    overflow: hidden;
    background: var(--bg);
  }
  .canvas {
    position: relative;
    width: 1200px;
    height: 1200px;
  }
  .label {
    position: absolute;
    left: 300px;
    top: 70px;
    width: 600px;
    height: 1060px;
    background: var(--label-white);
    border-radius: 36px;
    overflow: hidden;
    box-shadow: 0 4px 18px rgba(0,0,0,0.08);
  }
  .leaf-band {
    position: absolute;
    left: 0; top: 0;
    width: 600px;
    height: 360px;
    background: linear-gradient(160deg, var(--leaf-mid) 0%, var(--leaf-dark) 55%, var(--leaf-light) 100%);
  }
  .band-arc {
    position: absolute;
    left: 0; top: 300px;
    width: 600px;
    height: 110px;
  }
  .brand {
    position: absolute;
    top: 410px;
    left: 0;
    width: 600px;
    display: flex;
    justify-content: center;
    align-items: center;
    gap: 14px;
  }
  .brand-dot {
    width: 26px; height: 26px;
    border-radius: 50%;
    background: var(--brand-red);
  }
  .brand-name {
    font-family: "Cinzel", serif;
    font-weight: 600;
    font-size: 30px;
    letter-spacing: 2px;
    color: var(--brand-red);
  }
  .product-title {
    position: absolute;
    top: 480px;
    left: 0;
    width: 600px;
    text-align: center;
    font-family: "Cinzel", serif;
    line-height: 1;
  }
  .product-title .kind {
    display: block;
    font-size: 58px;
    font-weight: 400;
    color: var(--brand-red);
  }
  .product-title .item {
    display: block;
    margin-top: 8px;
    font-size: 108px;
    font-weight: 600;
    color: var(--title-green);
  }
  .local-name {
    position: absolute;
    top: 680px;
    left: 0;
    width: 600px;
    text-align: center;
    font-family: "Cinzel", serif;
    font-size: 20px;
    letter-spacing: 6px;
    color: var(--body-grey);
  }
  .description {
    position: absolute;
    top: 740px;
    left: 60px;
    width: 480px;
    text-align: center;
    font-family: "Open Sans", sans-serif;
    font-size: 17px;
    line-height: 1.4;
    color: var(--body-grey);
  }
  .net-weight {
    position: absolute;
    left: 50px;
    top: 930px;
    font-family: "Open Sans", sans-serif;
    font-size: 22px;
    line-height: 1.35;
    color: #333333;
  }
  .natural-seal {
    position: absolute;
    right: 46px;
    top: 910px;
    width: 96px;
    height: 96px;
    border-radius: 50%;
    background: var(--seal-green);
  }
</style>
</head>
<body>
<div class="canvas">
  <div class="label">
    <div class="leaf-band" role="img" aria-label="Pattern of stylised green sweet potato leaves"></div>
    <svg class="band-arc" viewBox="0 0 600 110" aria-hidden="true">
      <path d="M0 110 L0 60 Q300 -20 600 60 L600 110 Z" fill="var(--label-white)"/>
      <path d="M110 48 Q300 -8 490 48" fill="none" stroke="var(--brand-red)" stroke-width="4"/>
    </svg>
    <div class="brand">
      <span class="brand-dot"></span>
      <span class="brand-name">SAVANNA PANTRY</span>
    </div>
    <h1 class="product-title">
      <span class="kind">SWEET POTATO</span>
      <span class="item">LEAVES</span>
    </h1>
    <p class="local-name">(METAMBELE)</p>
    <p class="description">Lorem ipsum dolor sit amet, consectetuer adipiscing elit, sed diam nonummy nibh euismod tincidunt ut laoreet dolore magna aliquam erat</p>
    <p class="net-weight">Net Wt.<br>500 g</p>
    <div class="natural-seal" role="img" aria-label="All-natural seal"></div>
  </div>
</div>
</body>
</html>
```